wedding invitation card

Requirement:
1. White background, pink elements on the card, simple elegant looking
2. content:
Please join us as we celebrate new beginnings, new dreams,
and most importantly, new love at the marriage of
Miss Lin Qiao and Mr. Haoran Mu
Friday, The First of January
Two Thousand Fifteen at Eleven o’clock
Coral Tide Resort Palm Breeze Garden.

Reception will be followed at Lotus Hall at Half-Past Twelve o'clock

Please RSVP before December 18th 2015 by email: qiaolin0815@mailvexa.com

3. Flat paper
4. be able to change the size of the design according to printing requirement

Industry/Entity Type

Wedding

```html
<!DOCTYPE html>
<html lang="en">
<head>
<meta charset="utf-8">
<title>Wedding Invitation – Lin Qiao &amp; Haoran Mu</title>
<link rel="stylesheet" href="https://fonts.googleapis.com/css2?family=Caveat:wght@400&family=Pinyon+Script&display=swap">
<style>
  :root {
    --paper: #ffffff;
    --ink: #231815;
    --rose: #d4819f;
    --blossom-deep: #c0394f;
    --blossom-soft: #eab8c6;
  }
  html, body {
    margin: 0;
    padding: 0;
    width: 1200px;
    height: 927px;
    overflow: hidden;
    background: var(--paper);
  }
  .invitation {
    position: relative;
    width: 1200px;
    height: 927px;
    background: var(--paper);
    color: var(--ink);
    font-family: "Caveat", cursive;
  }
  .invitation__frame {
    position: absolute;
    left: 58px;
    top: 60px;
    width: 1092px;
    height: 790px;
    border: 1.5px solid var(--rose);
    box-sizing: border-box;
  }
  .invitation__intro {
    position: absolute;
    top: 128px;
    left: 0;
    width: 100%;
    margin: 0;
    text-align: center;
    font-size: 41px;
    line-height: 64px;
  }
  .invitation__couple {
    position: absolute;
    top: 318px;
    left: 0;
    width: 100%;
    margin: 0;
    text-align: center;
    font-family: "Pinyon Script", cursive;
    font-weight: 400;
    font-size: 68px;
    line-height: 100px;
    white-space: nowrap;
  }
  .invitation__ampersand {
    display: inline-block;
    color: var(--rose);
    font-size: 118px;
    vertical-align: -14px;
    margin: 0 -6px;
  }
  .invitation__date {
    position: absolute;
    top: 482px;
    left: 0;
    width: 100%;
    margin: 0;
    text-align: center;
    font-size: 32px;
    line-height: 48px;
  }
  .invitation__details {
    position: absolute;
    left: 106px;
    top: 668px;
    margin: 0;
    font-size: 22px;
    line-height: 49px;
  }
  .invitation__details p { margin: 0; }
  .invitation__blossoms {
    position: absolute;
    left: 956px;
    top: 672px;
    width: 194px;
    height: 178px;
    background: radial-gradient(ellipse at 80% 85%, var(--blossom-deep) 0%, var(--blossom-soft) 55%, rgba(255,255,255,0) 80%);
    opacity: 0.7;
  }
</style>
</head>
<body>
  <main class="invitation">
    <div class="invitation__frame"></div>

    <p class="invitation__intro">
      Please join us as we celebrate new beginnings, new dreams,<br>
      and most importantly, new love at the marriage of
    </p>

    <h1 class="invitation__couple">
      <span class="invitation__bride">Miss Lin Qiao</span><span class="invitation__ampersand">&amp;</span><span class="invitation__groom">Mr. Haoran Mu</span>
    </h1>

    <p class="invitation__date">
      Friday, The First of January<br>
      Two Thousand Sixteen at Eleven o’clock
    </p>

    <div class="invitation__details">
      <p>Coral Tide Resort Palm Breeze Garden.</p>
      <p>Reception will be followed at Lotus Hall at Half-Past Twelve o’clock</p>
      <p>Please RSVP before December 18th 2015 by email: qiaolin0815@mailvexa.com</p>
    </div>

    <div class="invitation__blossoms" role="img" aria-label="Illustration of red and pink blossoms on slender curved stems rising from the corner"></div>
  </main>
</body>
</html>
```